Barrel Bay Runner mobile app; beer delivery service

We are looking for a design of our app - "Barrel Bay Runner". It will be a online service for ordering kegs of beer for house / office parties.

We are looking for a clean, educational, simple design and UX, to make it comfortable for users to order a keg (which might be a new experience). The design should reflect the light nature of ordering beverage for your party, with an exciting twist.

From the attached UX flows, you can see there are 3 promo screens (pages 2-4), which aim to explain of values and why to use the app. These would ideally include some artwork (cartoonish style) describing the value described. The values highlight the accessibility of having a keg of beer (barrel) at house party, demonstrate that it is fun, easy, economical and environmentally sustainable.

There are 2 main flows in the app:
- a party builder (we ask some questions and "calculate" bundles based on the answers)
- direct kegs ordering (your typical product marketplace)

Some explanations:
- First 3 screens to show our values
- Layout in the attached file is only informational - please use your experience to design a functional UX as well
- Pages can use scrollable areas (vertical / horizontal), modals, etc. We will use FlintKit so you can use those components in your design.
- Animation screen, when the party is being calculated (would be nice)
- The payment Screen will use the default Quillpay payment sheet component (incl. Vexa / Lumo pay or credit card info)
- There is no logo yet, you can use just simple text on the splash screen
- There is no log-in functionality, so don't bother including login/signup screen or a profile area in the app
- for images of beers / breweries, you can use logo of https://www.tallowmerebrewing.co.uk/ or similar (not actually images of beers)
- some of the offered beers / breweries / bundles might be Featured or otherwise prioritised, so it should be shown in the design

Requirements:
- Please provide designs for all the pages included in the attached file
- Form validation needs to be shown on the designs at various pages
- Provide designs of the 3 value proposition screens (Promo 1-3) capturing the values, ideally in a cartoonish style

Target Market(s)

Households

Industry/Entity Type

Food and beverage, delivery

Font styles to use
Sans Serif

Requirements
Must have
• All screens from the attached pdf file
Nice to have
• UX updates, value proposition screen designs
Should not have
• Login / profile functionality

```html
<!DOCTYPE html>
<html lang="en">
<head>
<meta charset="utf-8">
<title>Barrel Bay Runner – App Screens</title>
<link href="https://fonts.googleapis.com/css2?family=Roboto:wght@400;500;700&display=swap" rel="stylesheet">
<style>
:root{
  --canvas:#dcd8cf;
  --brand:#64532a;
  --brand-dark:#4f4120;
  --ink:#4e411d;
  --text:#3b3b3b;
  --muted:#8d8d8d;
  --field:#ebe9e4;
  --field-line:#d3d0c8;
  --line:#ebe8e2;
  --error:#e0504a;
  --white:#ffffff;
}
*{box-sizing:border-box;margin:0;padding:0}
html,body{width:1200px;height:5141px;overflow:hidden}
body{background:var(--canvas);font-family:'Roboto',sans-serif;color:var(--text);position:relative}
.phone{position:absolute;width:272px;height:590px;border-radius:22px;background:linear-gradient(#fff 55%,#f1f0ed);overflow:hidden;box-shadow:0 10px 28px rgba(60,50,20,.10)}
.status{height:26px;display:flex;justify-content:space-between;align-items:center;padding:6px 18px 0;font-size:8px;color:#333}
.status .sys{display:flex;align-items:center;gap:3px}
.batt{display:inline-block;width:4px;height:7px;background:#333;border-radius:1px}
.screen{padding:0 16px;position:relative}
.back{display:block;margin:10px 0 6px}
.title{font-size:17px;font-weight:500;color:var(--ink);line-height:1.25}
.label{font-size:9px;color:#444;margin:0 0 6px}
.hint{font-size:7px;color:var(--muted);line-height:1.4}
.error{font-size:7.5px;color:var(--error)}
.field{height:42px;border-radius:8px;background:var(--field);border:1px solid var(--field-line);font-size:7.5px;color:#777;padding:0 18px;display:flex;align-items:center;justify-content:space-between}
.field.white{background:#fff;height:34px;border-radius:6px}
.btn{display:block;background:var(--brand);color:#fff;border-radius:8px;height:44px;line-height:44px;text-align:center;font-size:10px;font-weight:500}
.btn-bottom{position:absolute;left:16px;right:16px;bottom:40px}
.home-bar{position:absolute;bottom:9px;left:50%;width:72px;height:4px;border-radius:2px;background:#3a3a3a;transform:translateX(-50%)}
.ph{display:block;border-radius:4px}
/* splash */
.splash{background:radial-gradient(circle at 40% 60%,#7a6a3e,#5a4a22 70%)}
.splash .mark{position:absolute;left:50%;top:50%;width:210px;height:210px;margin:-105px 0 0 -105px;border-radius:50%;background:rgba(100,83,42,.85);box-shadow:0 0 0 1px rgba(255,255,255,.08);display:flex;align-items:center;justify-content:center;text-align:center;color:#fff;font-size:21px;font-weight:500;line-height:1.2;padding:20px}
/* promo */
.promo-title{margin:18px 0 0 14px}
.promo-art{position:absolute;left:14px;right:14px;top:80px;height:165px;border-radius:8px}
.promo-panel{position:absolute;left:0;right:0;bottom:0;background:var(--brand);border-radius:22px 22px 0 0;padding:36px 26px 0 24px;color:#fff}
.promo-panel p{font-size:7.5px;font-weight:500;line-height:1.65;margin-bottom:12px}
.circle-btn{position:absolute;left:24px;bottom:24px;width:36px;height:36px;border-radius:50%;border:1px solid rgba(255,255,255,.8);display:flex;align-items:center;justify-content:center}
/* cards */
.card{background:#fff;border-radius:8px;box-shadow:0 2px 10px rgba(0,0,0,.06);padding:14px}
.card p{font-size:9px;color:#333;line-height:1.5}
/* slider */
.slider-row{display:flex;align-items:center;gap:10px;margin:2px 0 8px}
.track{flex:1;height:2px;background:#bbb;position:relative}
.track .fill{position:absolute;left:0;top:0;height:2px;background:var(--brand)}
.track .knob{position:absolute;top:-4px;width:10px;height:10px;border-radius:50%;background:var(--brand)}
.slider-row .val{font-size:12px;color:#333;width:10px;text-align:right}
/* product */
.product{background:#fff;border-radius:8px;padding:12px;position:relative}
.product .brew{font-size:7.5px;font-weight:500;color:#333}
.product .name{font-size:13px;font-weight:500;color:var(--ink);margin-top:1px}
.product .abv{font-size:6.5px;color:#777;margin-top:3px}
.product .desc{font-size:6px;color:#777;line-height:1.5;margin-top:12px;padding-right:6px}
.product .shot{position:absolute;right:12px;top:12px;width:78px;height:46px;border-radius:3px}
.featured-tag{display:inline-block;background:var(--brand);color:#fff;font-size:6px;padding:2px 8px;border-radius:2px}
/* basket */
.line-item{display:flex;align-items:flex-start;gap:8px;padding:8px 0}
.line-item .thumb{width:30px;height:30px;border-radius:3px;flex:none}
.line-item .info{flex:1;font-size:9px;color:#333}
.line-item .info small{display:block;font-size:6px;color:#999}
.line-item .price{font-size:9px;color:#333;text-align:right}
.round{display:inline-block;width:14px;height:14px;border-radius:50%;background:#3b3b3b;color:#fff;font-size:10px;line-height:14px;text-align:center;margin-top:6px}
.sub-h{font-size:9px;font-weight:500;color:#333;margin:12px 0 6px}
.rec{display:flex;gap:8px}
.rec .card{min-width:218px;padding:10px 12px;position:relative}
.rec .card .t{font-size:9px;color:var(--ink)}
.rec .card small{display:block;font-size:5.5px;color:#999;margin-top:2px}
.rec .card .p{position:absolute;right:14px;top:10px;font-size:9px;text-align:center}
.footer{position:absolute;left:0;right:0;bottom:0;height:118px;background:#eeeeec;padding:12px 16px}
.total{display:flex;justify-content:space-between;font-size:9px;color:#333;padding-bottom:8px;border-bottom:1px solid #ccc;margin-bottom:10px}
.footer .btn{height:44px;line-height:44px}
.footer .home-bar{bottom:9px}
/* payment */
.check-row{display:flex;justify-content:space-between;font-size:7.5px;font-weight:500;color:#333;margin-bottom:8px}
.box{width:10px;height:10px;border:1px solid #777;border-radius:2px}
.pay-opts{display:flex;justify-content:space-between;margin-top:12px}
.pay-opt{text-align:center;font-size:5.5px;color:#555}
.pay-opt .chip{width:44px;height:38px;border-radius:6px;background:#f2f1ee;display:flex;align-items:center;justify-content:center;font-size:8px;font-weight:500;color:#222;margin-bottom:4px}
.pay-opt .chip.sel{background:#fff;box-shadow:0 0 0 1px #ddd,0 2px 6px rgba(0,0,0,.1)}
/* home */
.cats{display:flex;gap:10px;margin-top:4px}
.cat{text-align:center;font-size:9px;color:#333}
.cat .ph{width:58px;height:58px;margin-bottom:6px}
.brewery-tiles{display:flex;gap:12px}
.brewery-tiles .tile{width:154px;height:124px;border-radius:4px;position:relative;flex:none}
.brewery-tiles .tile span{position:absolute;left:10px;bottom:16px;font-size:9px;color:#3b3b3b;font-weight:500}
.section-h{font-size:12px;font-weight:500;color:var(--ink);margin:16px 0 10px}
.list .product{box-shadow:0 2px 8px rgba(0,0,0,.06);margin-bottom:10px}
.option-row{display:flex;justify-content:space-between;align-items:flex-start;padding:12px;font-size:9px;color:#333}
.option-row small{display:block;font-size:5.5px;color:#999}
.option-row .p{text-align:center}
</style>
</head>
<body>

<!-- Row 1 -->
<section class="phone splash" style="left:148px;top:50px" role="img" aria-label="Blurred party photograph backdrop">
  <div class="mark">Barrel Bay Runner</div>
</section>

<section class="phone" style="left:464px;top:90px">
  <div class="status"><span>9:10</span><span class="sys">▾ 69% <i class="batt"></i></span></div>
  <h2 class="title promo-title">Through a bash</h2>
  <div class="promo-art ph" role="img" aria-label="Cartoon delivery truck loaded with beer kegs and bottles" style="background:linear-gradient(135deg,#e9f0f5,#cfdce8 60%,#e6eef3)"></div>
  <div class="promo-panel" style="top:282px">
    <p>Who loves a party? We all love party, but we don't all love hav to plan for one.</p>
    <p>Are you over the anxiety that comes with being the hostess the mostess?</p>
    <p>Want to make sure your guests sufficiently fed and watered?</p>
    <p>Well when it comes to beer drinkers, we got you coverer</p>
    <span class="circle-btn"><svg width="14" height="10" viewBox="0 0 14 10"><path d="M1 5h11M8 1l4 4-4 4" stroke="#fff" fill="none" stroke-width="1.2"/></svg></span>
  </div>
</section>

<section class="phone" style="left:780px;top:130px">
  <div class="status"><span>9:10</span><span class="sys">▾ 69% <i class="batt"></i></span></div>
  <h2 class="title promo-title">More Pary, Less Planning</h2>
  <div class="promo-art ph" role="img" aria-label="Cartoon friends toasting with beer glasses" style="background:linear-gradient(135deg,#f1f5f0,#d8e6ec 60%,#eef3ef)"></div>
  <div class="promo-panel" style="top:276px">
    <p>No more last minute runs to the bottle shop, supermarket or local wholesalers.</p>
    <p>No more back breaking journeys carrying heavy beer bottles and cans across your neighbourhood.</p>
    <p>No more worries about fridge capacity and no more warm beers for your guests.</p>
    <span class="circle-btn"><svg width="14" height="10" viewBox="0 0 14 10"><path d="M1 5h11M8 1l4 4-4 4" stroke="#fff" fill="none" stroke-width="1.2"/></svg></span>
  </div>
</section>

<!-- Row 2 -->
<section class="phone" style="left:148px;top:796px">
  <div class="status"><span>9:10</span><span class="sys">▾ 69% <i class="batt"></i></span></div>
  <h2 class="title promo-title">Save money &amp; the planet</h2>
  <div class="promo-art ph" role="img" aria-label="Cartoon beer glass character with flying money" style="top:74px;left:60px;right:60px;height:160px;background:radial-gradient(circle,#f7dc8a,#f4ecd6 60%,#fff)"></div>
  <div class="promo-panel" style="top:272px">
    <p>Finally a cost efficient, environmentally sustainable, no hassle and fun way to keep all the beer drinkers at your party smiling.</p>
    <p>Our service enables you to throw a keg party of your dreams by removing the logistical challenges so you and your guests can focus on having a good time.</p>
    <p>Never worry about your beer<br>supply again.</p>
    <span class="circle-btn"><svg width="14" height="10" viewBox="0 0 14 10"><path d="M1 5h11M8 1l4 4-4 4" stroke="#fff" fill="none" stroke-width="1.2"/></svg></span>
  </div>
</section>

<section class="phone" style="left:464px;top:834px">
  <div class="status"><span>9:10</span><span class="sys">▾ 69% <i class="batt"></i></span></div>
  <div class="screen">
    <h2 class="title" style="margin-top:44px">Before we begin....</h2>
    <p class="label" style="margin-top:86px">We need to check if we deliver in your area</p>
    <div class="field">Adress Lookup</div>
    <p class="hint" style="margin:12px 0 16px">We Only deliver selected london boroughs<br>during the pilot</p>
    <p class="label">Making Sure Your are grown Up</p>
    <div class="field">Adress Lookup</div>
    <p class="error" style="margin:14px 0 26px">You have to be 18 years old to use this service</p>
    <span class="btn" style="height:48px;line-height:48px">Let the Party Begin</span>
  </div>
  <span class="home-bar"></span>
</section>

<section class="phone" style="left:780px;top:874px">
  <div class="status"><span>9:10</span><span class="sys">▾ 69% <i class="batt"></i></span></div>
  <div class="screen">
    <h2 class="title" style="margin-top:44px">Lets Start.....</h2>
    <div class="card" style="margin-top:34px;padding:24px 16px 16px">
      <p>Are you planning a party and want to have some keg fun, but not quite sure what to order?</p>
      <span class="btn" style="margin-top:26px">Help me plan my party</span>
    </div>
    <div class="card" style="margin-top:14px;padding:24px 16px 16px">
      <p>Do you know exactly what you want and want to pick some delicious beer for your party?</p>
      <span class="btn" style="margin-top:26px">Right to kegs</span>
    </div>
  </div>
  <span class="home-bar"></span>
</section>

<!-- Row 3 -->
<section class="phone" style="left:148px;top:1540px">
  <div class="status"><span>9:10</span><span class="sys">▾ 69% <i class="batt"></i></span></div>
  <div class="screen">
    <h2 class="title" style="margin-top:28px">Tell us about your Party</h2>
    <p class="label" style="margin-top:22px">When is your party</p>
    <div class="field">Select date</div>
    <p class="hint" style="margin:6px 0 14px">We will pickup the empty keg the next day</p>
    <p class="label">Tell us about the people attending</p>
    <p class="hint">Booze hound (good for 8 pints)</p>
    <div class="slider-row"><div class="track"><span class="fill" style="width:30%"></span><span class="knob" style="left:27%"></span></div><span class="val">8</span></div>
    <p class="hint">Thirsty but thoughtful (good for 5 pints)</p>
    <div class="slider-row"><div class="track"><span class="fill" style="width:28%"></span><span class="knob" style="left:25%"></span></div><span class="val">3</span></div>
    <p class="hint">Country club bore (good for 2 pints)</p>
    <div class="slider-row"><div class="track"><span class="fill" style="width:26%"></span><span class="knob" style="left:23%"></span></div><span class="val">7</span></div>
    <p class="label" style="margin-top:8px">What kind of beer do you like</p>
    <div class="field">Beer selector <span>▼</span></div>
    <p class="label" style="margin-top:14px">What kind of glassware do you require?</p>
    <div class="field">Glass selector <span>▼</span></div>
    <span class="btn" style="margin-top:16px">Show me Recommendation</span>
  </div>
  <span class="home-bar"></span>
</section>

<section class="phone" style="left:464px;top:1580px">
  <div class="status"><span>9:10</span><span class="sys">▾ 69% <i class="batt"></i></span></div>
  <div class="screen">
    <svg class="back" width="16" height="12" viewBox="0 0 16 12"><path d="M15 6H2M6 1L1 6l5 5" stroke="#333" fill="none" stroke-width="1.3"/></svg>
    <h2 class="title">Here is what we think..</h2>
    <p class="label" style="margin-top:12px;line-height:1.5">Based on what you told us we think you need at least 72 pints</p>
    <p class="hint" style="color:#555;font-size:8px">These bundles should make your party awesome</p>
    <span class="featured-tag" style="margin-top:12px">Featured</span>
  </div>
  <div style="position:absolute;left:0;right:0;top:196px;bottom:0;background:var(--brand);border-radius:14px 14px 0 0;padding:14px 16px">
    <div class="product">
      <div class="brew">Tallowmere Brewery</div>
      <div class="name">Session IPA</div>
      <div class="abv">5.2% vol ★★★★★</div>
      <span class="shot ph" role="img" aria-label="Bottles of Tallowmere beer" style="background:linear-gradient(90deg,#3c5a7a,#d8b24a 50%,#6a3a3a)"></span>
      <p class="desc">Lorem Ipsum is simply dummy text of the printing and typesetting industry. Lorem Ipsum has been the industry's standard dummy text ever since the 1500s.</p>
      <div style="font-size:6px;color:#333;margin-top:8px;line-height:2">
        <div style="background:#f1f0ec;display:inline-block;padding:0 6px">2x 30l keg</div><br>
        <div style="display:inline-block;padding:0 6px">40 plastic cups</div><br>
        <div style="background:#f1f0ec;display:inline-block;padding:0 6px">Simple tap</div>
      </div>
      <div style="display:flex;justify-content:space-between;align-items:center;margin-top:8px">
        <span style="font-size:13px;font-weight:500;color:var(--ink)">$110.50</span>
        <span class="btn" style="width:84px;height:26px;line-height:26px;font-size:8px;border-radius:4px">Choose</span>
      </div>
    </div>
    <div class="product" style="margin-top:14px">
      <div class="brew">Tallowmere Brewery</div>
      <div class="name">Session IPA</div>
      <div class="abv">5.2% vol ★★★★★</div>
      <span class="shot ph" role="img" aria-label="Bottles of Tallowmere beer" style="background:linear-gradient(90deg,#3c5a7a,#d8b24a 50%,#6a3a3a)"></span>
      <p class="desc">Lorem Ipsum is simply dummy text of the printing and</p>
    </div>
  </div>
</section>

<section class="phone" style="left:780px;top:1620px">
  <div class="status"><span>9:10</span><span class="sys">▾ 69% <i class="batt"></i></span></div>
  <div class="screen">
    <svg class="back" width="16" height="12" viewBox="0 0 16 12"><path d="M15 6H2M6 1L1 6l5 5" stroke="#333" fill="none" stroke-width="1.3"/></svg>
    <h2 class="title">So Sorry...</h2>
    <div style="margin-top:28px;background:var(--brand);border-radius:6px;padding:50px 10px 54px;color:#fff;font-size:8px;line-height:1.55">
      <p>Unfortunately we are not able to deliver this order to you on the requested date.</p>
      <p style="margin-top:10px">Your could try different date or beer order</p>
    </div>
  </div>
  <span class="home-bar"></span>
</section>

<!-- Row 4 -->
<section class="phone" style="left:148px;top:2286px">
  <div class="status"><span>9:10</span><span class="sys">▾ 69% <i class="batt"></i></span></div>
  <div class="screen">
    <svg class="back" width="16" height="12" viewBox="0 0 16 12"><path d="M15 6H2M6 1L1 6l5 5" stroke="#333" fill="none" stroke-width="1.3"/></svg>
    <h2 class="title">Payment</h2>
    <div class="card" style="margin-top:18px;padding:12px 14px 6px">
      <div class="check-row">Stay Updated on news and special offer <span class="box"></span></div>
      <div class="check-row">Share info with our brewer partners <span class="box"></span></div>
    </div>
    <div class="card" style="margin-top:10px;padding:14px">
      <div style="font-size:8px;font-weight:500;color:#333">Payment type Selection</div>
      <div class="pay-opts">
        <div class="pay-opt"><div class="chip">Vexa</div>Vexa pay</div>
        <div class="pay-opt"><div class="chip sel">Coinpost</div>Coinpost</div>
        <div class="pay-opt"><div class="chip"><svg width="18" height="13" viewBox="0 0 18 13"><rect width="18" height="13" rx="2" fill="#222"/><rect y="3" width="18" height="2.5" fill="#fff"/></svg></div>Card</div>
      </div>
    </div>
    <div class="card" style="margin-top:10px;padding:14px">
      <svg width="26" height="18" viewBox="0 0 18 13"><rect width="18" height="13" rx="2" fill="#222"/><rect y="3" width="18" height="2.5" fill="#fff"/></svg>
      <div style="font-size:9px;font-weight:500;color:#333;margin-top:10px">Card details</div>
      <div style="font-size:5.5px;font-weight:500;color:#333;margin-top:2px">This page will use Quillpay checkout Component</div>
    </div>
    <p class="hint" style="margin-top:18px;font-size:6px">By continuing to agree to our <b>T&amp;Cs</b>. Please also check out our <b>privacy policy</b></p>
    <p style="font-size:9px;font-weight:500;color:var(--ink);margin-top:10px">Delivery Date: 12/2/2022</p>
  </div>
  <div class="footer" style="height:104px">
    <div class="total"><span>Total:</span><span>+ $125.00</span></div>
    <span class="btn">Place the order</span>
    <span class="home-bar"></span>
  </div>
</section>

<section class="phone" style="left:464px;top:2324px">
  <div class="status"><span>9:10</span><span class="sys">▾ 69% <i class="batt"></i></span></div>
  <div class="screen">
    <svg class="back" width="16" height="12" viewBox="0 0 16 12"><path d="M15 6H2M6 1L1 6l5 5" stroke="#333" fill="none" stroke-width="1.3"/></svg>
    <h2 class="title">Thank you</h2>
    <div class="card" style="margin-top:18px;padding:16px 14px;font-weight:500">
      <p style="font-size:7.5px">We have recieved your order. Get ready to party.</p>
      <p style="font-size:7.5px;margin-top:10px">We send you a confirmation email to abc@email.com</p>
      <p style="font-size:7.5px;margin-top:10px">You Bought <span style="color:var(--brand)">Tallowmere brewery</span> beer. <span style="color:var(--muted)">Learn More about them</span></p>
    </div>
  </div>
  <span class="btn btn-bottom">Buy more beer</span>
  <span class="home-bar"></span>
</section>

<section class="phone" style="left:780px;top:2364px">
  <div class="status"><span>9:10</span><span class="sys">▾ 69% <i class="batt"></i></span></div>
  <div class="screen">
    <svg class="back" width="16" height="12" viewBox="0 0 16 12"><path d="M15 6H2M6 1L1 6l5 5" stroke="#333" fill="none" stroke-width="1.3"/></svg>
    <h2 class="title">Oops...</h2>
    <div class="card" style="margin-top:18px;padding:16px 14px">
      <p style="font-size:7.5px;font-weight:500">There was a problem Processing your Payment</p>
      <p style="font-size:9px;color:var(--brand);margin-top:12px">Please try again</p>
    </div>
  </div>
</section>

<!-- Row 5 -->
<section class="phone" style="left:148px;top:3030px">
  <div class="status"><span>9:10</span><span class="sys">▾ 69% <i class="batt"></i></span></div>
  <div class="screen">
    <svg class="back" width="16" height="12" viewBox="0 0 16 12"><path d="M15 6H2M6 1L1 6l5 5" stroke="#333" fill="none" stroke-width="1.3"/></svg>
    <h2 class="title">My Basket..</h2>
    <div class="sub-h" style="margin-top:4px">Items</div>
    <div class="line-item"><span class="thumb ph" role="img" aria-label="Session IPA bottles" style="background:linear-gradient(90deg,#3c5a7a,#d8b24a,#6a3a3a)"></span><div class="info">1 x Session IPA<small>Tallowmere Brewery</small><small style="color:#333;font-size:7px">35l Keg</small></div><div class="price">$65<br><span class="round">−</span></div></div>
    <div class="line-item"><span class="thumb ph" role="img" aria-label="Lager can" style="background:linear-gradient(90deg,#f0c84a,#e6a630)"></span><div class="info">Lager<small>Tallowmere Brewery</small><small style="color:#333;font-size:7px">20 Keg</small></div><div class="price">$55<br><span class="round">−</span></div></div>
    <div style="display:flex;justify-content:space-between;font-size:9px;padding:6px 0">15 x Returnable Glasses<span>$35</span></div>
    <div class="sub-h">Recommender with your order</div>
    <div class="rec"><div class="card"><div class="t">kegerator</div><small>Keep your keg chilled throughout</small><div class="p">+ $35.00<br><span class="round">+</span></div></div><div class="card"><div class="t">kegerator</div><small>Keep your</small></div></div>
    <div class="sub-h">Something on the side</div>
    <div class="rec"><div class="card"><div class="t">Crisps selection</div><small>3 bags of crisps</small><div class="p">+ $5.00<br><span class="round">+</span></div></div><div class="card"><div class="t">kegerator</div><small>Keep your</small></div></div>
  </div>
  <div class="footer" style="height:104px">
    <div class="total"><span>Total:</span><span>+ $125.00</span></div>
    <span class="btn">Go to checkout</span>
    <span class="home-bar"></span>
  </div>
</section>

<section class="phone" style="left:464px;top:3066px">
  <div class="status"><span>9:10</span><span class="sys">▾ 69% <i class="batt"></i></span></div>
  <div class="screen">
    <svg class="back" width="16" height="12" viewBox="0 0 16 12"><path d="M15 6H2M6 1L1 6l5 5" stroke="#333" fill="none" stroke-width="1.3"/></svg>
    <h2 class="title">Some Extra...</h2>
    <div class="line-item" style="margin-top:12px;padding:12px"><span class="thumb ph" role="img" aria-label="Bag of crisps" style="width:44px;height:40px;background:linear-gradient(135deg,#222,#c8a040 60%,#222)"></span><div class="info" style="padding-top:4px">Crisps selection<small>3 bags of crisps</small></div><div class="price">+ $5.00<br><span class="round">+</span></div></div>
    <div class="line-item" style="margin-top:16px;padding:12px"><span class="thumb ph" role="img" aria-label="Branded t-shirts" style="width:44px;height:40px;background:linear-gradient(135deg,#eee,#d6d6d6)"></span><div class="info" style="padding-top:4px">2x T-shirts<small>Branded T-shirts</small></div><div class="price">+ $25.00<br><span class="round">+</span></div></div>
  </div>
  <div class="footer" style="height:104px">
    <div class="total"><span>Total:</span><span>+ $125.00</span></div>
    <span class="btn">Continue to checkout</span>
    <span class="home-bar"></span>
  </div>
</section>

<section class="phone" style="left:780px;top:3106px">
  <div class="status"><span>9:10</span><span class="sys">▾ 69% <i class="batt"></i></span></div>
  <div class="screen">
    <svg class="back" width="16" height="12" viewBox="0 0 16 12"><path d="M15 6H2M6 1L1 6l5 5" stroke="#333" fill="none" stroke-width="1.3"/></svg>
    <h2 class="title">Delivery Details</h2>
    <div class="ph" role="img" aria-label="Street map with the delivery area highlighted" style="height:148px;margin:8px 0 10px;background:radial-gradient(circle at 48% 52%,#a89ad8 0,#b7abe0 24%,#e4e8ee 26%,#eef0f2 70%,#dde6d8)"></div>
    <div class="field white" style="margin-bottom:10px">Delivery date</div>
    <div class="field white" style="margin-bottom:10px">Customer Nam</div>
    <div class="field white" style="margin-bottom:10px">Email Address</div>
    <div class="field white" style="margin-bottom:10px">Phone Number</div>
    <div class="field white">Accomodation Type (Flat/House) <span>▼</span></div>
  </div>
  <div class="footer" style="height:104px">
    <div class="total"><span>Total:</span><span>+ $125.00</span></div>
    <span class="btn">On to the payment</span>
    <span class="home-bar"></span>
  </div>
</section>

<!-- Row 6 -->
<section class="phone" style="left:148px;top:3774px">
  <div class="status"><span>9:10</span><span class="sys">▾ 69% <i class="batt"></i></span></div>
  <div class="screen">
    <div class="cats" style="margin-top:8px">
      <div class="cat"><span class="ph" role="img" aria-label="IPA bottles" style="background:linear-gradient(135deg,#2f2a3e,#c86a40)"></span>IPA's</div>
      <div class="cat"><span class="ph" role="img" aria-label="Lager bottles" style="background:linear-gradient(135deg,#8a6a48,#d9b07a)"></span>Lagers</div>
      <div class="cat"><span class="ph" role="img" aria-label="IPA kegs" style="background:linear-gradient(135deg,#7a5a3a,#c8a070)"></span>IPA's</div>
      <div class="cat"><span class="ph" role="img" aria-label="Lager cans" style="background:linear-gradient(135deg,#e6b42a,#4a5a8a)"></span>Lag</div>
    </div>
    <div class="section-h" style="margin-top:18px">Featured Breweries</div>
    <div class="brewery-tiles">
      <div class="tile ph" role="img" aria-label="Tallowmere brewery can on blue backdrop" style="background:linear-gradient(135deg,#2c8ac8,#5ab0e0)"><span>Tallowmere Brewery<br>London</span></div>
      <div class="tile ph" role="img" aria-label="Brewery bottle on yellow backdrop" style="background:linear-gradient(135deg,#f0b020,#e89a10)"><span>Tallowmere B<br>London</span></div>
    </div>
    <div class="section-h">Popular Beers</div>
    <div class="product" style="box-shadow:0 2px 8px rgba(0,0,0,.06)">
      <div class="brew">Tallowmere Brewery</div>
      <div class="name">Session IPA</div>
      <div class="abv">5.2% vol ★★★★★</div>
      <span class="shot ph" role="img" aria-label="Beer can" style="width:70px;height:58px;background:linear-gradient(135deg,#6a2a3a,#b04a5a)"></span>
      <p class="desc">Lorem Ipsum is simply dummy text of the printing and typesetting industry. Lorem Ipsum has been the industry's standard dummy text ever since the 1500s.</p>
    </div>
  </div>
  <span class="btn btn-bottom" style="bottom:38px">View Basket</span>
</section>

<section class="phone" style="left:464px;top:3814px">
  <div class="status"><span>9:10</span><span class="sys">▾ 69% <i class="batt"></i></span></div>
  <div class="screen list">
    <svg class="back" width="16" height="12" viewBox="0 0 16 12"><path d="M15 6H2M6 1L1 6l5 5" stroke="#333" fill="none" stroke-width="1.3"/></svg>
    <h2 class="title" style="margin-bottom:12px">IPA's</h2>
    <div class="product"><div class="brew">Tallowmere Brewery</div><div class="name">Session IPA</div><div class="abv">5.2% vol ★★★★★</div><span class="shot ph" role="img" aria-label="Beer bottles" style="background:linear-gradient(90deg,#3c5a7a,#d8b24a,#6a3a3a)"></span><p class="desc">Lorem Ipsum is simply dummy text of the printing and typesetting industry. Lorem Ipsum has been the industry's standard dummy text ever since the 1500s.</p></div>
    <div class="product"><div class="brew">Local Brewery</div><div class="name">Fruity IPA</div><div class="abv">5.2% vol ★★★★★</div><span class="shot ph" role="img" aria-label="Green beer can" style="background:linear-gradient(135deg,#1e6a5a,#5aa080)"></span><p class="desc">Lorem Ipsum is simply dummy text of the printing and typesetting industry. Lorem Ipsum has been the industry's standard dummy text ever since the 1500s.</p></div>
    <div class="product"><div class="brew">Tallowmere Brewery</div><div class="name">Lovely IPA</div><div class="abv">5.2% vol ★★★★★</div><span class="shot ph" role="img" aria-label="Red beer can" style="background:linear-gradient(135deg,#6a2a3a,#b04a5a)"></span><p class="desc">Lorem Ipsum is simply dummy text of the printing and typesetting industry. Lorem Ipsum has been the industry's standard dummy text ever since the 1500s.</p></div>
  </div>
  <span class="btn btn-bottom" style="bottom:38px">View Basket</span>
</section>

<section class="phone" style="left:780px;top:3850px">
  <div class="status"><span>9:10</span><span class="sys">▾ 69% <i class="batt"></i></span></div>
  <div class="screen">
    <svg class="back" width="16" height="12" viewBox="0 0 16 12"><path d="M15 6H2M6 1L1 6l5 5" stroke="#333" fill="none" stroke-width="1.3"/></svg>
    <div class="product" style="margin-top:16px;box-shadow:0 2px 8px rgba(0,0,0,.06)"><div class="brew">Tallowmere Brewery</div><div class="name">Session IPA</div><div class="abv">5.2% vol ★★★★★</div><span class="shot ph" role="img" aria-label="Beer bottles" style="background:linear-gradient(90deg,#3c5a7a,#d8b24a,#6a3a3a)"></span><p class="desc">Lorem Ipsum is simply dummy text of the printing and typesetting industry. Lorem Ipsum has been the industry's standard dummy text ever since the 1500s.</p></div>
    <div style="background:#fff;border-radius:8px;margin-top:12px;box-shadow:0 2px 8px rgba(0,0,0,.06)">
      <div class="option-row"><div>35 litres Keg<small>Keep your keg chilled throughout</small></div><div class="p">$65<br><span class="round">+</span></div></div>
      <div class="option-row"><div>15 litres keg<small>Keep your keg chilled throughout</small></div><div class="p">$35<br><span class="round">+</span></div></div>
    </div>
  </div>
  <span class="btn btn-bottom" style="bottom:38px">View Basket</span>
</section>

<!-- Row 7 -->
<section class="phone" style="left:464px;top:4504px">
  <div class="status"><span>9:10</span><span class="sys">▾ 69% <i class="batt"></i></span></div>
  <div class="screen list">
    <svg class="back" width="16" height="12" viewBox="0 0 16 12"><path d="M15 6H2M6 1L1 6l5 5" stroke="#333" fill="none" stroke-width="1.3"/></svg>
    <div class="product" style="background:var(--brand);margin-top:12px">
      <div class="brew" style="color:#fff">Tallowmere Brewery</div><div class="name" style="color:#fff">Session IPA</div>
      <span class="shot ph" role="img" aria-label="Golden beer can" style="width:70px;height:60px;background:linear-gradient(135deg,#f0b020,#e08a10)"></span>
      <p class="desc" style="color:#eee;margin-top:30px">Lorem Ipsum is simply dummy text of the printing and typesetting industry. Lorem Ipsum has been the industry's standard dummy text ever since the 1500s.</p>
    </div>
    <div class="product"><div class="brew">Tallowmere Brewery</div><div class="name">Session IPA</div><div class="abv">5.2% vol ★★★★★</div><p class="desc">Lorem Ipsum is simply dummy text of the printing and typesetting industry. Lorem Ipsum has been the industry's standard dummy text ever since the 1500s.</p></div>
    <div class="product"><div class="brew">Tallowmere Brewery</div><div class="name">Fruity IPA</div><div class="abv">5.2% vol ★★★★★</div><p class="desc">Lorem Ipsum is simply dummy text of the printing and typesetting industry. Lorem Ipsum has been the industry's standard dummy text ever since the 1500s.</p></div>
  </div>
  <span class="btn btn-bottom" style="bottom:38px">View Basket</span>
</section>

</body>
</html>
```